BRISKWAY ELECTRICAL SIGN

We are wanting a sign to mount on the side of the road to attract peoples attention, it will be 1200mm high by 2400mm wide. We want it to stand out from the others, modern sharp looking, We are an electrical contractor who wants to be the market leader and supplier of choice to our current clients and futre clients.

Industry/Entity Type

Electrical

Colors

Designer to choose colors to be used in the design.

Requirements
Must have
• Name: Briskway Electrical
• Our logo as per uploaded files
• The words: Design - Installation - Maintenance
• Freecall: 0800 342 958
• Mobile : 021 736 4192 (delete mobile number if gets to cluttered)
• Web: www.briskway.net.nz
Should not have
• a light bulb, or plug

```html
<!DOCTYPE html>
<html lang="en">
<head>
<meta charset="utf-8">
<title>Briskway Electrical – Roadside Sign</title>
<link href="https://fonts.googleapis.com/css2?family=Montserrat:wght@600;700;800&display=swap" rel="stylesheet">
<style>
  :root {
    --backdrop: #231f20;
    --sky-light: #e6f0fb;
    --sky-mid: #bcd6f0;
    --sky-deep: #8fbde6;
    --brand-blue: #1d56ae;
    --brand-green: #97c11a;
    --dot-green: #c7dd5a;
    --ink: #111111;
    --white: #ffffff;
  }
  * { margin: 0; padding: 0; box-sizing: border-box; }
  html, body {
    width: 1200px; height: 1200px; overflow: hidden;
    background: var(--backdrop);
    font-family: "Montserrat", sans-serif;
  }
  .canvas { position: relative; width: 1200px; height: 1200px; }
  .sign {
    position: absolute; left: 36px; top: 335px; width: 1128px; height: 564px;
    overflow: hidden;
    background: linear-gradient(90deg, var(--sky-deep) 0%, var(--sky-mid) 18%, var(--sky-light) 50%, var(--sky-mid) 82%, var(--sky-deep) 100%);
  }
  .sign-texture {
    position: absolute; inset: 0;
    background:
      radial-gradient(ellipse at 8% 35%, rgba(140,200,235,.55), transparent 45%),
      radial-gradient(ellipse at 95% 70%, rgba(140,210,235,.55), transparent 45%);
  }
  .brand-name {
    position: absolute; left: 132px; top: 70px; width: 880px;
    color: var(--brand-blue); font-weight: 800; text-align: center;
    line-height: 1;
  }
  .brand-name .primary { display: block; font-size: 132px; letter-spacing: 2px; }
  .brand-name .secondary { display: block; font-size: 72px; letter-spacing: 4px; margin-top: 14px; }
  .services {
    position: absolute; left: 73px; top: 382px; width: 982px; height: 63px;
    background: var(--brand-blue); border: 3px solid var(--white); border-radius: 12px;
    display: flex; align-items: center; justify-content: center; gap: 16px;
    color: var(--white); font-weight: 800; font-size: 39px; letter-spacing: .5px;
  }
  .services .dot { width: 22px; height: 22px; border-radius: 50%; background: var(--dot-green); }
  .services-shadow {
    position: absolute; left: 150px; top: 440px; width: 830px; height: 40px;
    background: radial-gradient(ellipse at 50% 20%, rgba(20,40,70,.35), transparent 65%);
  }
  .freecall-band {
    position: absolute; left: 0; top: 488px; width: 584px; height: 76px;
    background: var(--brand-green);
    clip-path: polygon(0 0, 551px 0, 584px 100%, 0 100%);
  }
  .freecall {
    position: absolute; left: 38px; top: 500px;
    font-weight: 700; font-size: 37px; color: var(--ink); letter-spacing: .5px;
    white-space: nowrap;
  }
  .contact {
    position: absolute; top: 509px; display: flex; align-items: center; gap: 5px;
    font-weight: 700; font-size: 26px; color: var(--ink); white-space: nowrap;
  }
  .contact svg { width: 20px; height: 20px; flex: none; }
  .contact-mobile { left: 576px; }
  .contact-web { left: 807px; }
</style>
</head>
<body>
<div class="canvas">
  <div class="sign">
    <div class="sign-texture" role="img" aria-label="Soft light-blue hexagon network pattern"></div>

    <h1 class="brand-name">
      <span class="primary">BRISKWAY</span>
      <span class="secondary">ELECTRICAL</span>
    </h1>

    <div class="services-shadow"></div>
    <div class="services">
      <span>DESIGN</span><span class="dot"></span>
      <span>INSTALLATION</span><span class="dot"></span>
      <span>MAINTENANCE</span>
    </div>

    <div class="freecall-band"></div>
    <p class="freecall">FREE CALL: 0800 342 958</p>

    <p class="contact contact-mobile">
      <svg viewBox="0 0 24 24" aria-hidden="true"><path fill="#1d56ae" d="M6.6 10.8c1.4 2.8 3.8 5.1 6.6 6.6l2.2-2.2c.3-.3.7-.4 1-.2 1.1.4 2.3.6 3.6.6.6 0 1 .4 1 1V20c0 .6-.4 1-1 1C10.6 21 3 13.4 3 4c0-.6.4-1 1-1h3.5c.6 0 1 .4 1 1 0 1.3.2 2.5.6 3.6.1.3 0 .7-.2 1z"/><path fill="none" stroke="#1d56ae" stroke-width="1.6" d="M14 3a7 7 0 0 1 7 7M14 6.5a3.5 3.5 0 0 1 3.5 3.5"/></svg>
      021 736 4192
    </p>
    <p class="contact contact-web">
      <svg viewBox="0 0 24 24" aria-hidden="true"><g fill="none" stroke="#1d56ae" stroke-width="1.8"><circle cx="12" cy="12" r="9.5"/><ellipse cx="12" cy="12" rx="4" ry="9.5"/><path d="M2.5 12h19M4 7h16M4 17h16"/></g></svg>
      www.briskway.net.nz
    </p>
  </div>
</div>
</body>
</html>
```